Verpackungen für ein Mundgel
Zielgruppe
Hallo Zusammen :-)
Wir sind eine kleine Vertriebsfirma und bringen ein neues innovatives Mundgel auf den Markt. Unsere Zielgruppen sind alle Personen mit Probleme im Mundraum (Aphthen, Zahnfleischentzündungen, Druckstellen...etc.).
Aufgabenstellung
Die Verpackung wird für ein neues Mundgel benötigt. Die Stanzvorlage ist mit angehängt. Wichtig ist, dass die Gestaltung vertikal angebracht wird. Das Produkt ist 100% rein natürlich (komplett ohne Chemie).
Vom Design her soll die Kernbotschaft (innovative Einwirkformel für das Zahnfleisch & 100% Heilkraft der Natur & Manuka Honig (ein Inhaltsstoff)) wiedergespiegelt werden. Es kann gerne ein modernes 'medizinisches' Design sein.
Der Produktname lautet 'Velisa Mundgel'. Es geht erstmal nur um das Design. Die Pflichttexte...etc. werden dem Gewinner später bekannt gegeben und können im Nachhinein noch auf die Verpackung mit angebracht werden.
Wir freuen uns schon jetzt auf Eure kreativen Vorschläge :-)

```html
<!DOCTYPE html>
<html lang="de">
<head>
<meta charset="utf-8">
<title>Velisa Mundgel – Faltschachtel Stanzvorlage</title>
<link rel="stylesheet" href="https://fonts.googleapis.com/css2?family=Jost:wght@300;400;700&family=Tinos&display=swap">
<style>
  :root {
    --paper: #ffffff;
    --cut-line: #2e2a6b;
    --fold-line: #39b7e6;
    --glue-line: #f6c58f;
    --brand-green: #5c9a3a;
    --band-green: #64a832;
    --ink-grey: #3e3e3e;
    --honey: #f2c500;
    --dim-grey: #555555;
    --leaf-light: #c9df8a;
    --leaf-mid: #9cc440;
    --lemon: #f0e84a;
  }
  html, body {
    margin: 0;
    padding: 0;
    width: 1200px;
    height: 888px;
    overflow: hidden;
    background: var(--paper);
  }
  .dieline {
    display: block;
    width: 1200px;
    height: 888px;
  }
  .cut { fill: none; stroke: var(--cut-line); stroke-width: 2; }
  .fold { fill: none; stroke: var(--fold-line); stroke-width: 2; }
  .glue-area { fill: none; stroke: var(--glue-line); stroke-width: 2; }
  .brand-name {
    font-family: "Jost", sans-serif;
    font-weight: 300;
    font-size: 86px;
    letter-spacing: 14px;
    fill: var(--ink-grey);
  }
  .product-type {
    font-family: "Jost", sans-serif;
    font-weight: 700;
    font-size: 38px;
    letter-spacing: 9px;
    fill: var(--brand-green);
  }
  .claim-band { fill: var(--band-green); }
  .claim-text {
    font-family: "Jost", sans-serif;
    font-weight: 700;
    font-size: 18px;
    letter-spacing: 2px;
    fill: #ffffff;
  }
  .usage-line {
    font-family: "Jost", sans-serif;
    font-weight: 400;
    font-size: 14.5px;
    letter-spacing: 0.6px;
    fill: var(--ink-grey);
  }
  .usage-line .highlight { font-weight: 700; fill: var(--brand-green); }
  .seal { fill: none; stroke: var(--honey); stroke-width: 4; }
  .dim-line { stroke: var(--dim-grey); stroke-width: 2; fill: none; }
  .dim-value {
    font-family: "Tinos", serif;
    font-size: 120px;
    fill: var(--dim-grey);
  }
  .dim-value--small { font-size: 110px; }
  .grain-label {
    font-family: "Tinos", serif;
    font-size: 110px;
    fill: var(--dim-grey);
  }
</style>
</head>
<body>
<svg class="dieline" viewBox="0 0 2224 1645" xmlns="http://www.w3.org/2000/svg" aria-label="Faltschachtel Velisa Mundgel, Stanzvorlage mit Maßen">
  <defs>
    <linearGradient id="swirl-panel" x1="0" y1="0" x2="1" y2="0">
      <stop offset="0" stop-color="var(--leaf-mid)"/>
      <stop offset="0.07" stop-color="var(--lemon)" stop-opacity="0.7"/>
      <stop offset="0.2" stop-color="var(--leaf-light)" stop-opacity="0.35"/>
      <stop offset="0.32" stop-color="#ffffff"/>
      <stop offset="0.8" stop-color="#ffffff"/>
      <stop offset="0.93" stop-color="var(--leaf-light)" stop-opacity="0.6"/>
      <stop offset="1" stop-color="var(--lemon)"/>
    </linearGradient>
    <linearGradient id="swirl-flap" x1="0" y1="0" x2="0" y2="1">
      <stop offset="0" stop-color="var(--leaf-mid)"/>
      <stop offset="0.35" stop-color="#ffffff"/>
      <stop offset="0.7" stop-color="var(--leaf-light)" stop-opacity="0.6"/>
      <stop offset="1" stop-color="var(--lemon)"/>
    </linearGradient>
  </defs>

  <!-- tuck flap -->
  <polygon class="glue-area" points="395,160 412,90 1428,90 1444,160"/>
  <polygon class="cut" points="415,181 445,70 1394,70 1423,181"/>

  <!-- back panel (blank) -->
  <rect class="fold" x="415" y="181" width="1013" height="272"/>

  <!-- upper dust flap -->
  <rect x="1428" y="178" width="337" height="280" fill="url(#swirl-flap)" role="img" aria-label="Weich verlaufender grün-gelber Wellenhintergrund"/>
  <path class="cut" d="M1428,181 H1642 V232 H1634 V403 H1642 V453 H1428"/>
  <path class="cut" d="M1642,186 C1690,192 1730,225 1746,257 V380 C1730,412 1690,445 1642,448"/>
  <line class="fold" x1="1635" y1="232" x2="1635" y2="403"/>
  <line class="fold" x1="1428" y1="181" x2="1428" y2="453"/>

  <!-- side glue flaps, upper row -->
  <polygon class="cut" points="415,458 387,458 365,479 254,508 254,635 365,647 387,675 415,675"/>
  <polygon class="cut" points="1423,453 1448,478 1585,493 1585,620 1474,650 1455,669 1423,669"/>

  <!-- lower side flaps -->
  <polygon class="cut" points="415,947 387,972 254,988 254,1114 365,1143 387,1164 415,1164"/>
  <polygon class="cut" points="1423,952 1452,952 1474,974 1585,1002 1585,1124 1452,1139 1423,1164"/>

  <!-- lower dust flap -->
  <rect x="76" y="675" width="700" height="283" fill="url(#swirl-flap)" role="img" aria-label="Weich verlaufender grün-gelber Wellenhintergrund"/>
  <path class="cut" d="M411,675 H196 V725 H207 V896 H196 V947 H411"/>
  <path class="cut" d="M196,681 C150,686 110,715 92,748 V872 C110,905 150,935 196,942"/>
  <line class="fold" x1="204" y1="727" x2="204" y2="896"/>

  <!-- inner top panel (upside down) -->
  <rect x="415" y="453" width="1008" height="222" fill="url(#swirl-panel)" role="img" aria-label="Grün-gelber Wellenverlauf als Hintergrund"/>
  <g transform="rotate(180 919 564)">
    <rect class="claim-band" x="1054" y="455" width="369" height="49"/>
    <text class="claim-text" x="1238" y="487" text-anchor="middle" textLength="340" lengthAdjust="spacingAndGlyphs">MIT NEUER INNOVATIVER FORMEL</text>
    <circle class="seal" cx="598" cy="563" r="90"/>
    <text class="brand-name" x="1018" y="593" text-anchor="middle">VELISA</text>
    <text class="product-type" x="1018" y="638" text-anchor="middle">MUNDGEL</text>
  </g>
  <rect class="fold" x="415" y="453" width="1008" height="222"/>

  <!-- front panel -->
  <rect x="411" y="675" width="1027" height="272" fill="url(#swirl-panel)" role="img" aria-label="Grün-gelber Wellenverlauf als Hintergrund"/>
  <rect class="claim-band" x="1049" y="676" width="389" height="49"/>
  <text class="claim-text" x="1231" y="708" text-anchor="middle" textLength="342" lengthAdjust="spacingAndGlyphs">MIT NEUER INNOVATIVER FORMEL</text>
  <circle class="seal" cx="594" cy="812" r="92"/>
  <text class="brand-name" x="1012" y="823" text-anchor="middle">VELISA</text>
  <text class="product-type" x="1015" y="867" text-anchor="middle">MUNDGEL</text>
  <text class="usage-line" x="1015" y="900" text-anchor="middle" textLength="577" lengthAdjust="spacingAndGlyphs">REIN NATÜRLICHES GEL MIT <tspan class="highlight">MANUKA-HONIG</tspan> ZUR ANWENDUNG IN DER MUNDHÖHLE</text>
  <rect class="fold" x="411" y="675" width="1012" height="272"/>

  <!-- bottom panel -->
  <rect x="415" y="947" width="1008" height="243" fill="url(#swirl-panel)" role="img" aria-label="Grün-gelber Wellenverlauf als Hintergrund"/>
  <rect class="claim-band" x="1053" y="950" width="370" height="49"/>
  <text class="claim-text" x="1237" y="982" text-anchor="middle" textLength="342" lengthAdjust="spacingAndGlyphs">MIT NEUER INNOVATIVER FORMEL</text>
  <circle class="seal" cx="597" cy="1057" r="90"/>
  <text class="brand-name" x="1016" y="1087" text-anchor="middle">VELISA</text>
  <text class="product-type" x="1018" y="1132" text-anchor="middle">MUNDGEL</text>
  <line class="fold" x1="415" y1="947" x2="415" y2="1164"/>
  <line class="fold" x1="1423" y1="947" x2="1423" y2="1164"/>
  <line class="cut" x1="387" y1="1164" x2="1423" y2="1164"/>

  <!-- dimensions -->
  <g class="dimensions">
    <line class="dim-line" x1="413" y1="1315" x2="1426" y2="1315"/>
    <polyline class="dim-line" points="452,1307 413,1315 452,1323"/>
    <polyline class="dim-line" points="1387,1307 1426,1315 1387,1323"/>
    <text class="dim-value" x="985" y="1302" text-anchor="middle">100</text>

    <line class="dim-line" x1="90" y1="1467" x2="1750" y2="1467"/>
    <polyline class="dim-line" points="130,1459 90,1467 130,1475"/>
    <polyline class="dim-line" points="1710,1459 1750,1467 1710,1475"/>
    <text class="dim-value" x="985" y="1454" text-anchor="middle">164</text>

    <line class="dim-line" x1="2048" y1="68" x2="2048" y2="1168"/>
    <polyline class="dim-line" points="2041,106 2048,68 2055,106"/>
    <polyline class="dim-line" points="2041,1130 2048,1168 2055,1130"/>
    <text class="dim-value" transform="translate(2060,705) rotate(90)" text-anchor="middle">108.5</text>

    <line class="dim-line" x1="1892" y1="179" x2="1892" y2="678"/>
    <polyline class="dim-line" points="1886,217 1892,179 1898,217"/>
    <polyline class="dim-line" points="1886,420 1892,458 1898,420"/>
    <polyline class="dim-line" points="1886,490 1892,453 1898,490"/>
    <polyline class="dim-line" points="1886,640 1892,678 1898,640"/>
    <text class="dim-value dim-value--small" transform="translate(1905,357) rotate(90)" text-anchor="middle">27</text>
    <text class="dim-value dim-value--small" transform="translate(1905,605) rotate(90)" text-anchor="middle">22</text>

    <text class="grain-label" transform="translate(1895,1250) rotate(90)" text-anchor="middle">&lt; Faserlauf &gt;</text>
  </g>
</svg>
</body>
</html>
```